Home delivery Premium Dog Food Company needs Facebook Profile picture cover photo

need artwork for profile pic and cover pic. profile should be 180 X 180 pixels or 540 X 540. cover needs to be 851 X 315 pixels saved as JPG and less than 100 kilobytes. Sugesstions: Integrate profile with cover photo...see 'velmora brisk' on facebook as example. please 'right' align cover photo. Another suggestion is incorporate an offer in cover photo; "Win a years supply of dog treats". please reference the FB specs photo included.

It Company

```html
<!DOCTYPE html>
<html lang="en">
<head>
<meta charset="utf-8">
<title>Harlow's Kitchen – Facebook profile and cover</title>
<link rel="stylesheet" href="https://fonts.googleapis.com/css2?family=Fredoka:wght@600&family=Oswald:wght@400&family=PT+Sans:wght@400&display=swap">
<style>
  :root {
    --stage-light: #ffffff;
    --stage-edge: #d8d8d8;
    --gold: #e2b43a;
    --gold-deep: #b07f25;
    --gold-bright: #f0c542;
    --ink: #17121a;
    --cover-dark: #232323;
    --cover-mid: #2d2d2d;
    --white: #ffffff;
    --url-ink: #2a2a2a;
    --food-brown: #6b4418;
  }
  * { box-sizing: border-box; margin: 0; padding: 0; }
  html, body { width: 1200px; height: 1000px; overflow: hidden; }
  body {
    position: relative;
    background: radial-gradient(ellipse 70% 65% at 50% 52%, var(--stage-light) 55%, var(--stage-edge) 100%);
    font-family: "Fredoka", "Arial Rounded MT Bold", sans-serif;
  }

  /* Profile picture */
  .profile {
    position: absolute; left: 483px; top: 165px; width: 238px; height: 238px;
    background: radial-gradient(circle at 50% 50%, var(--gold-bright) 0%, var(--gold) 45%, var(--gold-deep) 100%);
    display: flex; flex-direction: column; align-items: center; justify-content: center;
  }
  .profile__name {
    font-family: "Fredoka", sans-serif; font-weight: 600;
    color: var(--ink); font-size: 30px; line-height: 1; letter-spacing: 1px; text-align: center;
  }
  .profile__name span { display: block; font-size: 17px; letter-spacing: 3px; margin-top: 6px; }

  /* Cover photo */
  .cover {
    position: absolute; left: 177px; top: 479px; width: 851px; height: 315px;
    overflow: hidden; background: var(--cover-mid);
  }
  .cover__pattern {
    position: absolute; inset: 0;
    background: radial-gradient(ellipse 60% 80% at 50% 50%, var(--cover-dark) 0%, var(--cover-mid) 70%, #333333 100%);
  }
  .cover__badge { position: absolute; left: 38px; top: 0; width: 68px; height: 85px; }
  .cover__badge-text {
    position: absolute; left: 38px; top: 22px; width: 68px;
    font-family: "Oswald", sans-serif; font-weight: 400; font-size: 15px; line-height: 24px;
    color: var(--white); text-align: center; text-transform: uppercase;
    text-shadow: 1px 1px 1px rgba(0,0,0,0.45);
  }
  .cover__url { position: absolute; right: 0; top: 0; width: 175px; height: 23px; }
  .cover__url-text {
    position: absolute; right: 10px; top: 2px;
    font-family: "PT Sans", sans-serif; font-size: 13.5px; color: var(--url-ink);
  }
  .cover__tagline { position: absolute; left: 316px; top: 26px; width: 220px; height: 60px; }
  .cover__bowl {
    position: absolute; left: 346px; top: 60px; width: 159px; height: 46px;
    background: linear-gradient(180deg, var(--food-brown) 0%, var(--gold) 60%, var(--gold-deep) 100%);
  }
  .cover__offer {
    position: absolute; left: 0; right: 0; top: 112px;
    text-align: center; color: var(--white); text-transform: uppercase; font-weight: 600;
  }
  .cover__offer-win { font-size: 56px; line-height: 50px; letter-spacing: 2px; }
  .cover__offer-line { font-size: 33px; line-height: 41px; letter-spacing: 1.5px; }
  .cover__offer-line--first { margin-top: 4px; }
  .cover__paw {
    display: inline-block; width: 24px; height: 24px; border-radius: 50%;
    background: var(--gold); vertical-align: -1px; margin: 0 1px;
  }
</style>
</head>
<body>

  <section class="profile" aria-label="Profile picture">
    <p class="profile__name">HARLOW'S<span>KITCHEN</span></p>
  </section>

  <section class="cover" aria-label="Cover photo">
    <div class="cover__pattern" role="img" aria-label="Scattered paw prints and dog bones on a dark background"></div>

    <svg class="cover__badge" viewBox="0 0 68 85" aria-hidden="true">
      <defs>
        <linearGradient id="badgeGold" x1="0" y1="0" x2="1" y2="0">
          <stop offset="0" stop-color="#c8922c"/>
          <stop offset="0.5" stop-color="#e7b843"/>
          <stop offset="1" stop-color="#b07f25"/>
        </linearGradient>
      </defs>
      <polygon points="0,0 68,0 68,68 34,85 0,68" fill="url(#badgeGold)"/>
    </svg>
    <p class="cover__badge-text">Official<br>Page</p>

    <svg class="cover__url" viewBox="0 0 175 23" aria-hidden="true">
      <polygon points="0,0 175,0 175,23 14,23" fill="#e2b43a"/>
    </svg>
    <p class="cover__url-text">www.harlowskitchen.com</p>

    <svg class="cover__tagline" viewBox="0 0 220 60">
      <defs>
        <path id="taglineArc" d="M8,47 Q110,-18 212,49"/>
      </defs>
      <text font-family="PT Sans, sans-serif" font-size="14" fill="#e2b43a" letter-spacing="0.9">
        <textPath href="#taglineArc" startOffset="50%" text-anchor="middle">Quality is our main Ingredient</textPath>
      </text>
    </svg>
    <div class="cover__bowl" role="img" aria-label="Illustration of a gold dog bowl filled with kibble"></div>

    <div class="cover__offer">
      <p class="cover__offer-win">Win</p>
      <p class="cover__offer-line cover__offer-line--first">A years supply of</p>
      <p class="cover__offer-line">D<span class="cover__paw" role="img" aria-label="Paw print"></span>G treats</p>
    </div>
  </section>

</body>
</html>
```